Brochure Template

We are looking for a new brochure template which will allow us to key in the products.

We will fill in the specification of product in the empty spaces.

Size A2 size double fold. Total of 4 pp x A3 size.

Must be in .ai file (CS3) to be given. Must provide font type as well.

One page should fit at least 20 products.
Updates

Target Market(s)

Prepare brochure template similar to the attached design.

Industry/Entity Type

Product

Requirements
Must have
• Marketbay.com.bn logo

space for product picture preferably white background.
Nice to have
• must provide font type so that we can use the design as template.

```html
<!DOCTYPE html>
<html lang="en">
<head>
<meta charset="utf-8">
<title>Marketbay.com.bn – Product Brochure Template</title>
<link href="https://fonts.googleapis.com/css2?family=Archivo+Black&family=Roboto:wght@400;700;900&family=Roboto+Condensed:wght@400;700&display=swap" rel="stylesheet">
<style>
  :root{
    --blue:#0a3a9c;
    --blue-dark:#062a78;
    --yellow:#ffd21f;
    --cream:#fff4cf;
    --card:#fffaf0;
    --red:#e3141b;
    --ink:#222;
    --grey:#8a8f99;
    --rule:#e3c77a;
  }
  *{box-sizing:border-box;margin:0;padding:0}
  html,body{width:848px;height:1200px;overflow:hidden;background:#fff}
  body{font-family:"Roboto",Arial,sans-serif;color:var(--ink)}
  .page{width:848px;height:1200px;position:relative;background:var(--cream);overflow:hidden}

  .masthead{height:80px;background:linear-gradient(180deg,var(--blue) 0%,var(--blue-dark) 100%);
    display:flex;align-items:center;justify-content:space-between;padding:0 24px 0 22px;border-bottom:3px solid #fff}
  .masthead-title{font-family:"Archivo Black",sans-serif;color:#fff;font-size:44px;letter-spacing:1px;line-height:1}
  .store-name{display:flex;align-items:center;gap:10px}
  .store-name .mark{width:14px;height:14px;background:#fff;flex:none}
  .store-name .name{font-family:"Roboto",sans-serif;font-weight:700;font-size:22px;color:#fff;line-height:1}

  .product-grid{position:absolute;top:90px;left:10px;right:10px;height:1022px;
    display:grid;grid-template-columns:repeat(3,1fr);grid-template-rows:repeat(7,1fr);gap:4px 6px}
  .product-card{background:var(--card);border:1px solid var(--rule);position:relative;padding:5px 6px;display:flex;flex-direction:column;overflow:hidden}
  .card-top{display:flex;flex:1}
  .card-info{flex:1;min-width:0}
  .card-title{color:var(--red);font-weight:700;font-size:12px;line-height:14px;white-space:nowrap}
  .spec-list{list-style:none;margin-top:2px}
  .spec-list li{font-family:"Roboto Condensed",sans-serif;font-size:7.5px;line-height:10px;color:#333;white-space:nowrap}
  .spec-list li::before{content:"• ";color:var(--red)}
  .card-media{width:120px;position:relative;flex:none}
  .price{color:var(--red);font-family:"Roboto",sans-serif;font-weight:900;font-size:24px;line-height:24px;text-align:right;padding-right:4px}
  .product-photo{position:absolute;left:4px;top:28px;width:70px;height:52px;border-radius:6px;
    background:radial-gradient(circle at 55% 55%,#3a3a3a 0 30%,#111 60%,#555 100%)}
  .deal-badge{position:absolute;right:0;top:40px;width:30px;height:30px;border-radius:50%;background:var(--red);
    color:#fff;font-size:6.5px;font-weight:700;display:flex;align-items:center;justify-content:center;text-align:center;line-height:7px}
  .accessory-strip{height:32px;display:flex;gap:3px;align-items:flex-end;border-top:1px solid var(--rule);padding-top:3px}
  .strip-label{width:38px;height:26px;background:var(--grey);color:#fff;font-size:7px;font-weight:700;display:flex;align-items:center;justify-content:center;border-radius:2px}
  .accessory{flex:1;display:flex;flex-direction:column;align-items:center}
  .accessory .thumb{width:26px;height:15px;background:linear-gradient(180deg,#6b6f78,#2c2f35);border-radius:2px}
  .accessory .cap{font-size:5.5px;line-height:8px;color:#555}

  .footer{position:absolute;left:0;right:0;bottom:0;height:78px;background:linear-gradient(180deg,var(--blue) 0%,var(--blue-dark) 100%);
    display:flex;align-items:center;color:#fff;padding:0 16px;border-top:3px solid #fff}
  .footer-block{font-size:10px;line-height:13px;padding:0 14px;white-space:nowrap}
  .footer-block .web{color:var(--yellow)}
  .footer-divider{width:1px;height:48px;background:rgba(255,255,255,.6)}
  .footer-title{font-family:"Archivo Black",sans-serif;font-size:26px;padding:0 20px;line-height:1;white-space:nowrap}
  .footer-block.center{text-align:center}
</style>
</head>
<body>
<div class="page">
  <header class="masthead">
    <h1 class="masthead-title">LOREM IMPSUM</h1>
    <div class="store-name"><span class="mark"></span><span class="name">Marketbay.com.bn</span></div>
  </header>

  <main class="product-grid">
    <article class="product-card"><div class="card-top"><div class="card-info"><h2 class="card-title">Lorem Impsum</h2><ul class="spec-list"><li>Lorem ipsum dolor</li><li>Sit amet consec</li><li>Adipis elit sed</li><li>Ut enim ad</li><li>Minim veniam quis</li><li>Nostrud exercit</li></ul></div><div class="card-media"><div class="price">$000</div><div class="product-photo" role="img" aria-label="Product photo: camera"></div><div class="deal-badge">Lorem<br>ipsum</div></div></div><div class="accessory-strip"><div class="strip-label">Lorem</div><div class="accessory"><div class="thumb" role="img" aria-label="Accessory photo"></div><span class="cap">Lorem</span></div><div class="accessory"><div class="thumb" role="img" aria-label="Accessory photo"></div><span class="cap">Ipsum</span></div><div class="accessory"><div class="thumb" role="img" aria-label="Accessory photo"></div><span class="cap">Dolor</span></div><div class="accessory"><div class="thumb" role="img" aria-label="Accessory photo"></div><span class="cap">Amet</span></div><div class="accessory"><div class="thumb" role="img" aria-label="Accessory photo"></div><span class="cap">Elit</span></div></div></article>
    <article class="product-card"><div class="card-top"><div class="card-info"><h2 class="card-title">Lorem Impsum</h2><ul class="spec-list"><li>Lorem ipsum dolor</li><li>Sit amet consec</li><li>Adipis elit sed</li><li>Ut enim ad</li><li>Minim veniam quis</li><li>Nostrud exercit</li></ul></div><div class="card-media"><div class="price">$000</div><div class="product-photo" role="img" aria-label="Product photo: camera"></div><div class="deal-badge">Lorem<br>ipsum</div></div></div><div class="accessory-strip"><div class="strip-label">Lorem</div><div class="accessory"><div class="thumb" role="img" aria-label="Accessory photo"></div><span class="cap">Lorem</span></div><div class="accessory"><div class="thumb" role="img" aria-label="Accessory photo"></div><span class="cap">Ipsum</span></div><div class="accessory"><div class="thumb" role="img" aria-label="Accessory photo"></div><span class="cap">Dolor</span></div><div class="accessory"><div class="thumb" role="img" aria-label="Accessory photo"></div><span class="cap">Amet</span></div><div class="accessory"><div class="thumb" role="img" aria-label="Accessory photo"></div><span class="cap">Elit</span></div></div></article>
    <article class="product-card"><div class="card-top"><div class="card-info"><h2 class="card-title">Lorem Impsum</h2><ul class="spec-list"><li>Lorem ipsum dolor</li><li>Sit amet consec</li><li>Adipis elit sed</li><li>Ut enim ad</li><li>Minim veniam quis</li><li>Nostrud exercit</li></ul></div><div class="card-media"><div class="price">$000</div><div class="product-photo" role="img" aria-label="Product photo: camera"></div><div class="deal-badge">Lorem<br>ipsum</div></div></div><div class="accessory-strip"><div class="strip-label">Lorem</div><div class="accessory"><div class="thumb" role="img" aria-label="Accessory photo"></div><span class="cap">Lorem</span></div><div class="accessory"><div class="thumb" role="img" aria-label="Accessory photo"></div><span class="cap">Ipsum</span></div><div class="accessory"><div class="thumb" role="img" aria-label="Accessory photo"></div><span class="cap">Dolor</span></div><div class="accessory"><div class="thumb" role="img" aria-label="Accessory photo"></div><span class="cap">Amet</span></div><div class="accessory"><div class="thumb" role="img" aria-label="Accessory photo"></div><span class="cap">Elit</span></div></div></article>
    <article class="product-card"><div class="card-top"><div class="card-info"><h2 class="card-title">Lorem Impsum</h2><ul class="spec-list"><li>Lorem ipsum dolor</li><li>Sit amet consec</li><li>Adipis elit sed</li><li>Ut enim ad</li><li>Minim veniam quis</li><li>Nostrud exercit</li></ul></div><div class="card-media"><div class="price">$000</div><div class="product-photo" role="img" aria-label="Product photo: camera"></div><div class="deal-badge">Lorem<br>ipsum</div></div></div><div class="accessory-strip"><div class="strip-label">Lorem</div><div class="accessory"><div class="thumb" role="img" aria-label="Accessory photo"></div><span class="cap">Lorem</span></div><div class="accessory"><div class="thumb" role="img" aria-label="Accessory photo"></div><span class="cap">Ipsum</span></div><div class="accessory"><div class="thumb" role="img" aria-label="Accessory photo"></div><span class="cap">Dolor</span></div><div class="accessory"><div class="thumb" role="img" aria-label="Accessory photo"></div><span class="cap">Amet</span></div><div class="accessory"><div class="thumb" role="img" aria-label="Accessory photo"></div><span class="cap">Elit</span></div></div></article>
    <article class="product-card"><div class="card-top"><div class="card-info"><h2 class="card-title">Lorem Impsum</h2><ul class="spec-list"><li>Lorem ipsum dolor</li><li>Sit amet consec</li><li>Adipis elit sed</li><li>Ut enim ad</li><li>Minim veniam quis</li><li>Nostrud exercit</li></ul></div><div class="card-media"><div class="price">$000</div><div class="product-photo" role="img" aria-label="Product photo: camera"></div><div class="deal-badge">Lorem<br>ipsum</div></div></div><div class="accessory-strip"><div class="strip-label">Lorem</div><div class="accessory"><div class="thumb" role="img" aria-label="Accessory photo"></div><span class="cap">Lorem</span></div><div class="accessory"><div class="thumb" role="img" aria-label="Accessory photo"></div><span class="cap">Ipsum</span></div><div class="accessory"><div class="thumb" role="img" aria-label="Accessory photo"></div><span class="cap">Dolor</span></div><div class="accessory"><div class="thumb" role="img" aria-label="Accessory photo"></div><span class="cap">Amet</span></div><div class="accessory"><div class="thumb" role="img" aria-label="Accessory photo"></div><span class="cap">Elit</span></div></div></article>
    <article class="product-card"><div class="card-top"><div class="card-info"><h2 class="card-title">Lorem Impsum</h2><ul class="spec-list"><li>Lorem ipsum dolor</li><li>Sit amet consec</li><li>Adipis elit sed</li><li>Ut enim ad</li><li>Minim veniam quis</li><li>Nostrud exercit</li></ul></div><div class="card-media"><div class="price">$000</div><div class="product-photo" role="img" aria-label="Product photo: camera"></div><div class="deal-badge">Lorem<br>ipsum</div></div></div><div class="accessory-strip"><div class="strip-label">Lorem</div><div class="accessory"><div class="thumb" role="img" aria-label="Accessory photo"></div><span class="cap">Lorem</span></div><div class="accessory"><div class="thumb" role="img" aria-label="Accessory photo"></div><span class="cap">Ipsum</span></div><div class="accessory"><div class="thumb" role="img" aria-label="Accessory photo"></div><span class="cap">Dolor</span></div><div class="accessory"><div class="thumb" role="img" aria-label="Accessory photo"></div><span class="cap">Amet</span></div><div class="accessory"><div class="thumb" role="img" aria-label="Accessory photo"></div><span class="cap">Elit</span></div></div></article>
    <article class="product-card"><div class="card-top"><div class="card-info"><h2 class="card-title">Lorem Impsum</h2><ul class="spec-list"><li>Lorem ipsum dolor</li><li>Sit amet consec</li><li>Adipis elit sed</li><li>Ut enim ad</li><li>Minim veniam quis</li><li>Nostrud exercit</li></ul></div><div class="card-media"><div class="price">$000</div><div class="product-photo" role="img" aria-label="Product photo: camera"></div><div class="deal-badge">Lorem<br>ipsum</div></div></div><div class="accessory-strip"><div class="strip-label">Lorem</div><div class="accessory"><div class="thumb" role="img" aria-label="Accessory photo"></div><span class="cap">Lorem</span></div><div class="accessory"><div class="thumb" role="img" aria-label="Accessory photo"></div><span class="cap">Ipsum</span></div><div class="accessory"><div class="thumb" role="img" aria-label="Accessory photo"></div><span class="cap">Dolor</span></div><div class="accessory"><div class="thumb" role="img" aria-label="Accessory photo"></div><span class="cap">Amet</span></div><div class="accessory"><div class="thumb" role="img" aria-label="Accessory photo"></div><span class="cap">Elit</span></div></div></article>
    <article class="product-card"><div class="card-top"><div class="card-info"><h2 class="card-title">Lorem Impsum</h2><ul class="spec-list"><li>Lorem ipsum dolor</li><li>Sit amet consec</li><li>Adipis elit sed</li><li>Ut enim ad</li><li>Minim veniam quis</li><li>Nostrud exercit</li></ul></div><div class="card-media"><div class="price">$000</div><div class="product-photo" role="img" aria-label="Product photo: camera"></div><div class="deal-badge">Lorem<br>ipsum</div></div></div><div class="accessory-strip"><div class="strip-label">Lorem</div><div class="accessory"><div class="thumb" role="img" aria-label="Accessory photo"></div><span class="cap">Lorem</span></div><div class="accessory"><div class="thumb" role="img" aria-label="Accessory photo"></div><span class="cap">Ipsum</span></div><div class="accessory"><div class="thumb" role="img" aria-label="Accessory photo"></div><span class="cap">Dolor</span></div><div class="accessory"><div class="thumb" role="img" aria-label="Accessory photo"></div><span class="cap">Amet</span></div><div class="accessory"><div class="thumb" role="img" aria-label="Accessory photo"></div><span class="cap">Elit</span></div></div></article>
    <article class="product-card"><div class="card-top"><div class="card-info"><h2 class="card-title">Lorem Impsum</h2><ul class="spec-list"><li>Lorem ipsum dolor</li><li>Sit amet consec</li><li>Adipis elit sed</li><li>Ut enim ad</li><li>Minim veniam quis</li><li>Nostrud exercit</li></ul></div><div class="card-media"><div class="price">$000</div><div class="product-photo" role="img" aria-label="Product photo: camera"></div><div class="deal-badge">Lorem<br>ipsum</div></div></div><div class="accessory-strip"><div class="strip-label">Lorem</div><div class="accessory"><div class="thumb" role="img" aria-label="Accessory photo"></div><span class="cap">Lorem</span></div><div class="accessory"><div class="thumb" role="img" aria-label="Accessory photo"></div><span class="cap">Ipsum</span></div><div class="accessory"><div class="thumb" role="img" aria-label="Accessory photo"></div><span class="cap">Dolor</span></div><div class="accessory"><div class="thumb" role="img" aria-label="Accessory photo"></div><span class="cap">Amet</span></div><div class="accessory"><div class="thumb" role="img" aria-label="Accessory photo"></div><span class="cap">Elit</span></div></div></article>
    <article class="product-card"><div class="card-top"><div class="card-info"><h2 class="card-title">Lorem Impsum</h2><ul class="spec-list"><li>Lorem ipsum dolor</li><li>Sit amet consec</li><li>Adipis elit sed</li><li>Ut enim ad</li><li>Minim veniam quis</li><li>Nostrud exercit</li></ul></div><div class="card-media"><div class="price">$000</div><div class="product-photo" role="img" aria-label="Product photo: camera"></div><div class="deal-badge">Lorem<br>ipsum</div></div></div><div class="accessory-strip"><div class="strip-label">Lorem</div><div class="accessory"><div class="thumb" role="img" aria-label="Accessory photo"></div><span class="cap">Lorem</span></div><div class="accessory"><div class="thumb" role="img" aria-label="Accessory photo"></div><span class="cap">Ipsum</span></div><div class="accessory"><div class="thumb" role="img" aria-label="Accessory photo"></div><span class="cap">Dolor</span></div><div class="accessory"><div class="thumb" role="img" aria-label="Accessory photo"></div><span class="cap">Amet</span></div><div class="accessory"><div class="thumb" role="img" aria-label="Accessory photo"></div><span class="cap">Elit</span></div></div></article>
    <article class="product-card"><div class="card-top"><div class="card-info"><h2 class="card-title">Lorem Impsum</h2><ul class="spec-list"><li>Lorem ipsum dolor</li><li>Sit amet consec</li><li>Adipis elit sed</li><li>Ut enim ad</li><li>Minim veniam quis</li><li>Nostrud exercit</li></ul></div><div class="card-media"><div class="price">$000</div><div class="product-photo" role="img" aria-label="Product photo: camera"></div><div class="deal-badge">Lorem<br>ipsum</div></div></div><div class="accessory-strip"><div class="strip-label">Lorem</div><div class="accessory"><div class="thumb" role="img" aria-label="Accessory photo"></div><span class="cap">Lorem</span></div><div class="accessory"><div class="thumb" role="img" aria-label="Accessory photo"></div><span class="cap">Ipsum</span></div><div class="accessory"><div class="thumb" role="img" aria-label="Accessory photo"></div><span class="cap">Dolor</span></div><div class="accessory"><div class="thumb" role="img" aria-label="Accessory photo"></div><span class="cap">Amet</span></div><div class="accessory"><div class="thumb" role="img" aria-label="Accessory photo"></div><span class="cap">Elit</span></div></div></article>
    <article class="product-card"><div class="card-top"><div class="card-info"><h2 class="card-title">Lorem Impsum</h2><ul class="spec-list"><li>Lorem ipsum dolor</li><li>Sit amet consec</li><li>Adipis elit sed</li><li>Ut enim ad</li><li>Minim veniam quis</li><li>Nostrud exercit</li></ul></div><div class="card-media"><div class="price">$000</div><div class="product-photo" role="img" aria-label="Product photo: camera"></div><div class="deal-badge">Lorem<br>ipsum</div></div></div><div class="accessory-strip"><div class="strip-label">Lorem</div><div class="accessory"><div class="thumb" role="img" aria-label="Accessory photo"></div><span class="cap">Lorem</span></div><div class="accessory"><div class="thumb" role="img" aria-label="Accessory photo"></div><span class="cap">Ipsum</span></div><div class="accessory"><div class="thumb" role="img" aria-label="Accessory photo"></div><span class="cap">Dolor</span></div><div class="accessory"><div class="thumb" role="img" aria-label="Accessory photo"></div><span class="cap">Amet</span></div><div class="accessory"><div class="thumb" role="img" aria-label="Accessory photo"></div><span class="cap">Elit</span></div></div></article>
    <article class="product-card"><div class="card-top"><div class="card-info"><h2 class="card-title">Lorem Impsum</h2><ul class="spec-list"><li>Lorem ipsum dolor</li><li>Sit amet consec</li><li>Adipis elit sed</li><li>Ut enim ad</li><li>Minim veniam quis</li><li>Nostrud exercit</li></ul></div><div class="card-media"><div class="price">$000</div><div class="product-photo" role="img" aria-label="Product photo: camera"></div><div class="deal-badge">Lorem<br>ipsum</div></div></div><div class="accessory-strip"><div class="strip-label">Lorem</div><div class="accessory"><div class="thumb" role="img" aria-label="Accessory photo"></div><span class="cap">Lorem</span></div><div class="accessory"><div class="thumb" role="img" aria-label="Accessory photo"></div><span class="cap">Ipsum</span></div><div class="accessory"><div class="thumb" role="img" aria-label="Accessory photo"></div><span class="cap">Dolor</span></div><div class="accessory"><div class="thumb" role="img" aria-label="Accessory photo"></div><span class="cap">Amet</span></div><div class="accessory"><div class="thumb" role="img" aria-label="Accessory photo"></div><span class="cap">Elit</span></div></div></article>
    <article class="product-card"><div class="card-top"><div class="card-info"><h2 class="card-title">Lorem Impsum</h2><ul class="spec-list"><li>Lorem ipsum dolor</li><li>Sit amet consec</li><li>Adipis elit sed</li><li>Ut enim ad</li><li>Minim veniam quis</li><li>Nostrud exercit</li></ul></div><div class="card-media"><div class="price">$000</div><div class="product-photo" role="img" aria-label="Product photo: camera"></div><div class="deal-badge">Lorem<br>ipsum</div></div></div><div class="accessory-strip"><div class="strip-label">Lorem</div><div class="accessory"><div class="thumb" role="img" aria-label="Accessory photo"></div><span class="cap">Lorem</span></div><div class="accessory"><div class="thumb" role="img" aria-label="Accessory photo"></div><span class="cap">Ipsum</span></div><div class="accessory"><div class="thumb" role="img" aria-label="Accessory photo"></div><span class="cap">Dolor</span></div><div class="accessory"><div class="thumb" role="img" aria-label="Accessory photo"></div><span class="cap">Amet</span></div><div class="accessory"><div class="thumb" role="img" aria-label="Accessory photo"></div><span class="cap">Elit</span></div></div></article>
    <article class="product-card"><div class="card-top"><div class="card-info"><h2 class="card-title">Lorem Impsum</h2><ul class="spec-list"><li>Lorem ipsum dolor</li><li>Sit amet consec</li><li>Adipis elit sed</li><li>Ut enim ad</li><li>Minim veniam quis</li><li>Nostrud exercit</li></ul></div><div class="card-media"><div class="price">$000</div><div class="product-photo" role="img" aria-label="Product photo: camera"></div><div class="deal-badge">Lorem<br>ipsum</div></div></div><div class="accessory-strip"><div class="strip-label">Lorem</div><div class="accessory"><div class="thumb" role="img" aria-label="Accessory photo"></div><span class="cap">Lorem</span></div><div class="accessory"><div class="thumb" role="img" aria-label="Accessory photo"></div><span class="cap">Ipsum</span></div><div class="accessory"><div class="thumb" role="img" aria-label="Accessory photo"></div><span class="cap">Dolor</span></div><div class="accessory"><div class="thumb" role="img" aria-label="Accessory photo"></div><span class="cap">Amet</span></div><div class="accessory"><div class="thumb" role="img" aria-label="Accessory photo"></div><span class="cap">Elit</span></div></div></article>
    <article class="product-card"><div class="card-top"><div class="card-info"><h2 class="card-title">Lorem Impsum</h2><ul class="spec-list"><li>Lorem ipsum dolor</li><li>Sit amet consec</li><li>Adipis elit sed</li><li>Ut enim ad</li><li>Minim veniam quis</li><li>Nostrud exercit</li></ul></div><div class="card-media"><div class="price">$000</div><div class="product-photo" role="img" aria-label="Product photo: camera"></div><div class="deal-badge">Lorem<br>ipsum</div></div></div><div class="accessory-strip"><div class="strip-label">Lorem</div><div class="accessory"><div class="thumb" role="img" aria-label="Accessory photo"></div><span class="cap">Lorem</span></div><div class="accessory"><div class="thumb" role="img" aria-label="Accessory photo"></div><span class="cap">Ipsum</span></div><div class="accessory"><div class="thumb" role="img" aria-label="Accessory photo"></div><span class="cap">Dolor</span></div><div class="accessory"><div class="thumb" role="img" aria-label="Accessory photo"></div><span class="cap">Amet</span></div><div class="accessory"><div class="thumb" role="img" aria-label="Accessory photo"></div><span class="cap">Elit</span></div></div></article>
    <article class="product-card"><div class="card-top"><div class="card-info"><h2 class="card-title">Lorem Impsum</h2><ul class="spec-list"><li>Lorem ipsum dolor</li><li>Sit amet consec</li><li>Adipis elit sed</li><li>Ut enim ad</li><li>Minim veniam quis</li><li>Nostrud exercit</li></ul></div><div class="card-media"><div class="price">$000</div><div class="product-photo" role="img" aria-label="Product photo: camera"></div><div class="deal-badge">Lorem<br>ipsum</div></div></div><div class="accessory-strip"><div class="strip-label">Lorem</div><div class="accessory"><div class="thumb" role="img" aria-label="Accessory photo"></div><span class="cap">Lorem</span></div><div class="accessory"><div class="thumb" role="img" aria-label="Accessory photo"></div><span class="cap">Ipsum</span></div><div class="accessory"><div class="thumb" role="img" aria-label="Accessory photo"></div><span class="cap">Dolor</span></div><div class="accessory"><div class="thumb" role="img" aria-label="Accessory photo"></div><span class="cap">Amet</span></div><div class="accessory"><div class="thumb" role="img" aria-label="Accessory photo"></div><span class="cap">Elit</span></div></div></article>
    <article class="product-card"><div class="card-top"><div class="card-info"><h2 class="card-title">Lorem Impsum</h2><ul class="spec-list"><li>Lorem ipsum dolor</li><li>Sit amet consec</li><li>Adipis elit sed</li><li>Ut enim ad</li><li>Minim veniam quis</li><li>Nostrud exercit</li></ul></div><div class="card-media"><div class="price">$000</div><div class="product-photo" role="img" aria-label="Product photo: camera"></div><div class="deal-badge">Lorem<br>ipsum</div></div></div><div class="accessory-strip"><div class="strip-label">Lorem</div><div class="accessory"><div class="thumb" role="img" aria-label="Accessory photo"></div><span class="cap">Lorem</span></div><div class="accessory"><div class="thumb" role="img" aria-label="Accessory photo"></div><span class="cap">Ipsum</span></div><div class="accessory"><div class="thumb" role="img" aria-label="Accessory photo"></div><span class="cap">Dolor</span></div><div class="accessory"><div class="thumb" role="img" aria-label="Accessory photo"></div><span class="cap">Amet</span></div><div class="accessory"><div class="thumb" role="img" aria-label="Accessory photo"></div><span class="cap">Elit</span></div></div></article>
    <article class="product-card"><div class="card-top"><div class="card-info"><h2 class="card-title">Lorem Impsum</h2><ul class="spec-list"><li>Lorem ipsum dolor</li><li>Sit amet consec</li><li>Adipis elit sed</li><li>Ut enim ad</li><li>Minim veniam quis</li><li>Nostrud exercit</li></ul></div><div class="card-media"><div class="price">$000</div><div class="product-photo" role="img" aria-label="Product photo: camera"></div><div class="deal-badge">Lorem<br>ipsum</div></div></div><div class="accessory-strip"><div class="strip-label">Lorem</div><div class="accessory"><div class="thumb" role="img" aria-label="Accessory photo"></div><span class="cap">Lorem</span></div><div class="accessory"><div class="thumb" role="img" aria-label="Accessory photo"></div><span class="cap">Ipsum</span></div><div class="accessory"><div class="thumb" role="img" aria-label="Accessory photo"></div><span class="cap">Dolor</span></div><div class="accessory"><div class="thumb" role="img" aria-label="Accessory photo"></div><span class="cap">Amet</span></div><div class="accessory"><div class="thumb" role="img" aria-label="Accessory photo"></div><span class="cap">Elit</span></div></div></article>
    <article class="product-card"><div class="card-top"><div class="card-info"><h2 class="card-title">Lorem Impsum</h2><ul class="spec-list"><li>Lorem ipsum dolor</li><li>Sit amet consec</li><li>Adipis elit sed</li><li>Ut enim ad</li><li>Minim veniam quis</li><li>Nostrud exercit</li></ul></div><div class="card-media"><div class="price">$000</div><div class="product-photo" role="img" aria-label="Product photo: camera"></div><div class="deal-badge">Lorem<br>ipsum</div></div></div><div class="accessory-strip"><div class="strip-label">Lorem</div><div class="accessory"><div class="thumb" role="img" aria-label="Accessory photo"></div><span class="cap">Lorem</span></div><div class="accessory"><div class="thumb" role="img" aria-label="Accessory photo"></div><span class="cap">Ipsum</span></div><div class="accessory"><div class="thumb" role="img" aria-label="Accessory photo"></div><span class="cap">Dolor</span></div><div class="accessory"><div class="thumb" role="img" aria-label="Accessory photo"></div><span class="cap">Amet</span></div><div class="accessory"><div class="thumb" role="img" aria-label="Accessory photo"></div><span class="cap">Elit</span></div></div></article>
    <article class="product-card"><div class="card-top"><div class="card-info"><h2 class="card-title">Lorem Impsum</h2><ul class="spec-list"><li>Lorem ipsum dolor</li><li>Sit amet consec</li><li>Adipis elit sed</li><li>Ut enim ad</li><li>Minim veniam quis</li><li>Nostrud exercit</li></ul></div><div class="card-media"><div class="price">$000</div><div class="product-photo" role="img" aria-label="Product photo: camera"></div><div class="deal-badge">Lorem<br>ipsum</div></div></div><div class="accessory-strip"><div class="strip-label">Lorem</div><div class="accessory"><div class="thumb" role="img" aria-label="Accessory photo"></div><span class="cap">Lorem</span></div><div class="accessory"><div class="thumb" role="img" aria-label="Accessory photo"></div><span class="cap">Ipsum</span></div><div class="accessory"><div class="thumb" role="img" aria-label="Accessory photo"></div><span class="cap">Dolor</span></div><div class="accessory"><div class="thumb" role="img" aria-label="Accessory photo"></div><span class="cap">Amet</span></div><div class="accessory"><div class="thumb" role="img" aria-label="Accessory photo"></div><span class="cap">Elit</span></div></div></article>
  </main>

  <footer class="footer">
    <div class="footer-block">Asimi ea et pa net officto selectatur!<br>Menit et us, quiatemquam estiore<br><span class="web">www.lorem.com</span></div>
    <div class="footer-divider"></div>
    <div class="footer-title">LOREM IMPSUM</div>
    <div class="footer-divider"></div>
    <div class="footer-block center"><span class="web">www.lorem.com</span><br>Asimi ea et pa net officto?</div>
    <div class="footer-divider"></div>
    <div class="footer-block">Asimi ea et pa net<br>officto selectatur<br>es at pa net officto</div>
  </footer>
</div>
</body>
</html>
```